Forward Systems Forum 2017 - Banner Ad Design

We are looking for a banner design for an event based out of Minneapolis Minnesota. Our company is hosting our annual Forward Systems Forum this fall at the Larkfield Arena and we are advertising on Wavecrest radio. On top of audio ads we are also doing a Banner Ad, which is what we need help creating! We would like to use the Larkfield Arena picture attached as a background and have "Forward Systems Forum 2017" or "FSF17" sticking out. However, we would like the stadium picture to be eye appealing and draw attention. The over all look is to draw our audience attention to want to click and learn more about the Systems Forum and hopefully sign up!

Target Market(s)

Men ages 30-55

Industry/Entity Type

Information Technology

Logo Text

Forward Systems Forum 2017

Colors
f78f20
9bcb3b
0255a3

Requirements
Must have
• "Forward Systems Forum 2017"
Nice to have
• The colors below are not a must but are our companys colors. Designers can feel free to use these and/or elegant colors as well! We are open to everything!

```html
<!DOCTYPE html>
<html lang="en">
<head>
<meta charset="utf-8">
<title>Forward Systems Forum 2017 – Banner</title>
<link href="https://fonts.googleapis.com/css2?family=Montserrat:wght@600;700&display=swap" rel="stylesheet">
<style>
  :root {
    --navy-deep: #121d33;
    --navy: #1f2c40;
    --slate: #3b4a4c;
    --haze: #9aa88c;
    --field: #34502a;
    --title-peach: #f8c88f;
    --year-white: #ffffff;
    --venue-blue: #1d4f9c;
    --venue-red: #d4202f;
    --host-ink: #2a2c2e;
    --host-accent: #f78f20;
  }
  html, body {
    margin: 0;
    padding: 0;
    width: 1200px;
    height: 566px;
    overflow: hidden;
    background: var(--navy-deep);
  }
  .banner {
    position: relative;
    width: 1200px;
    height: 566px;
    overflow: hidden;
    font-family: "Montserrat", sans-serif;
  }
  .arena-backdrop {
    position: absolute;
    inset: 0;
    background:
      radial-gradient(ellipse 520px 260px at 780px 40px, rgba(190,200,175,0.75), rgba(190,200,175,0) 70%),
      radial-gradient(ellipse 560px 200px at 720px 440px, rgba(70,110,50,0.85), rgba(70,110,50,0) 75%),
      radial-gradient(ellipse 420px 360px at 1100px 300px, rgba(90,120,70,0.55), rgba(90,120,70,0) 75%),
      linear-gradient(90deg, var(--navy-deep) 0%, var(--navy) 25%, var(--slate) 55%, var(--field) 100%);
  }
  .venue-mark {
    position: absolute;
    top: 54px;
    left: 0;
    width: 100%;
    display: flex;
    justify-content: center;
    align-items: center;
    gap: 12px;
  }
  .venue-square {
    width: 38px;
    height: 38px;
    background: var(--venue-red);
  }
  .venue-name {
    font-weight: 600;
    font-size: 44px;
    letter-spacing: -0.5px;
    color: var(--venue-blue);
  }
  .host-mark {
    position: absolute;
    top: 150px;
    left: 0;
    width: 100%;
    display: flex;
    justify-content: center;
    align-items: center;
    gap: 10px;
  }
  .host-square {
    width: 26px;
    height: 26px;
    background: var(--host-accent);
  }
  .host-name {
    font-weight: 700;
    font-size: 22px;
    letter-spacing: 0.5px;
    color: var(--host-ink);
    text-transform: uppercase;
  }
  .event-title {
    position: absolute;
    top: 236px;
    left: 0;
    width: 100%;
    margin: 0;
    text-align: center;
    font-weight: 700;
    font-size: 78px;
    line-height: 92px;
    letter-spacing: -1px;
    color: var(--title-peach);
  }
  .event-year {
    display: block;
    color: var(--year-white);
  }
</style>
</head>
<body>
  <div class="banner">
    <div class="arena-backdrop" role="img" aria-label="Interior of an empty domed arena with tiered seating and a green football field under a bright glass roof"></div>

    <div class="venue-mark">
      <span class="venue-square"></span>
      <span class="venue-name">Larkfield Arena</span>
    </div>

    <div class="host-mark">
      <span class="host-square"></span>
      <span class="host-name">Norvale Data Solutions</span>
    </div>

    <h1 class="event-title">
      Forward Systems<br>
      Forum
      <span class="event-year">2017</span>
    </h1>
  </div>
</body>
</html>
```